Summit Builders Web Site / Business Cards

Construction Company that specializes in Water and Fire Damage, Residential ReModels, Landscaping and Building ADU (Accessory Dwelling Unit)

Growing and changing families often need additional space, and a remodeling project can often provide that. Adding a new area, or repurposing an existing one can satisfy this requirement.

Other times, homeowners want to update the look in their kitchen or bathroom with more than just a change of cabinetry or vanity doors and drawers. Whatever your needs are, Summit Builders has skilled workers who are bonded and insured, and ready to make your dreams and visions a reality.

Target Market(s)

Home Owners

Industry/Entity Type

Construction Company

Contact Information for Business Card

Center Logo with our information on the corners

Back side to be Logo Only
Contact Info
CSLB License # 4829516
info@summitbuildersca.example
www.summitbuildersca.example

Coding

Coded - Design and coding required

Number of Pages Required

5+ page

Font styles to use
Serif
Sans Serif

Requirements
Must have
• Using our Logo Colors
Home
About Us
Services
Projects / Portfolio
Contact Us
Nice to have
• Colors matching our Logo
Should not have
• Black because it doesnt match our logo

```html
<!DOCTYPE html>
<html lang="en">
<head>
<meta charset="utf-8">
<title>Summit Builders</title>
<link href="https://fonts.googleapis.com/css2?family=Montserrat:wght@300;400;500;600;700;800&family=Raleway:wght@400;500;600&display=swap" rel="stylesheet">
<style>
:root{
  --orange:#ff6a13;
  --orange-deep:#f25c05;
  --ink:#111111;
  --text:#2a2a2a;
  --navy:#1d2733;
  --slate:#3a4756;
  --footer:#262626;
  --footer-rule:#5a5a5a;
  --white:#ffffff;
}
*{margin:0;padding:0;box-sizing:border-box}
html,body{width:1200px;height:3068px;overflow:hidden}
body{position:relative;background:var(--white);font-family:"Raleway",sans-serif;color:var(--text)}
.abs{position:absolute}

/* header + hero */
.hero-bg{left:0;top:0;width:1200px;height:660px}
.brand{left:157px;top:40px;color:var(--white);font-family:"Montserrat",sans-serif}
.brand-mark{display:inline-block;width:18px;height:18px;background:var(--orange);vertical-align:middle;margin-right:10px}
.brand-name{font-size:24px;font-weight:700;letter-spacing:2px;vertical-align:middle}
.nav{top:49px;left:530px;display:flex;gap:0;font-family:"Montserrat",sans-serif;font-size:12px;color:var(--white)}
.nav a{color:var(--white);text-decoration:none;position:absolute;white-space:nowrap}
.search{left:886px;top:49px}
.btn{background:var(--orange);color:var(--white);font-family:"Montserrat",sans-serif;font-size:12px;display:flex;align-items:center;justify-content:center;text-decoration:none}
.btn-contact{left:922px;top:38px;width:130px;height:39px;font-weight:500}
.hero-title{left:0;width:1200px;text-align:center;color:var(--white);font-family:"Montserrat",sans-serif}
.hero-title.big{top:222px;font-size:76px;font-weight:800;letter-spacing:-1px}
.hero-title.light{top:298px;font-size:56px;font-weight:300;letter-spacing:1px}
.hero-tag{top:370px;left:0;width:1200px;text-align:center;color:var(--white);font-family:"Montserrat",sans-serif;font-size:16px;letter-spacing:3.5px;font-weight:500}
.btn-hero{left:535px;top:409px;width:130px;height:39px}
.scroll-cue{left:588px;top:498px}

/* about */
.about-kicker{left:161px;top:680px;font-family:"Montserrat",sans-serif;font-size:15px;color:var(--ink)}
.about-title{left:161px;top:705px;font-family:"Montserrat",sans-serif;font-size:32px;font-weight:700;letter-spacing:5px;color:var(--ink)}
.about-copy{left:161px;top:778px;width:440px;font-size:11px;line-height:24px;color:var(--text)}
.about-copy p+p{margin-top:24px}
.btn-about{left:161px;top:1013px;width:130px;height:39px}
.about-photo{left:658px;top:683px}

/* stats */
.stat{display:flex;flex-direction:column;align-items:center;color:var(--white);font-family:"Montserrat",sans-serif}
.stat-num{font-size:40px;font-weight:300;margin-top:42px}
.stat-label{font-size:19px;font-weight:700;text-align:center;line-height:24px;margin-top:14px}
.stat-a{left:144px;top:1123px;width:300px;height:211px;background:linear-gradient(135deg,#2c343c,#1a1f24)}
.stat-b{left:444px;top:1119px;width:312px;height:220px;background:linear-gradient(135deg,#ff8a3d,var(--orange-deep))}
.stat-c{left:756px;top:1123px;width:301px;height:211px;background:linear-gradient(135deg,#3b3d3f,#222629)}

/* services */
.services-bg{left:0;top:1398px}
.svc-kicker{left:0;width:1200px;top:1502px;text-align:center;color:var(--white);font-family:"Montserrat",sans-serif;font-size:15px}
.svc-title{left:0;width:1200px;top:1528px;text-align:center;color:var(--white);font-family:"Montserrat",sans-serif;font-size:30px;font-weight:700;letter-spacing:5px}
.svc-intro{left:200px;width:800px;top:1587px;text-align:center;color:var(--white);font-size:11px;line-height:22px}
.svc-col{top:1705px;width:300px;display:flex;flex-direction:column;align-items:center;color:var(--white);text-align:center}
.svc-col h3{font-family:"Montserrat",sans-serif;font-size:19px;font-weight:600;margin-top:22px}
.svc-col p{font-size:11px;line-height:21px;margin-top:28px;width:260px}
.svc-col a{color:var(--white);font-size:11px;font-style:italic;margin-top:14px}
.svc-rule{top:1690px;width:1px;height:260px;background:rgba(255,255,255,.5)}

/* projects */
.proj-title{left:0;width:1200px;top:2122px;text-align:center;font-family:"Montserrat",sans-serif;font-size:32px;font-weight:700;letter-spacing:6px;color:var(--ink)}
.proj-intro{left:200px;width:800px;top:2182px;text-align:center;font-size:11px;line-height:23px;color:var(--text)}
.card{overflow:hidden}
.card-photo{width:100%;height:100%}
.card-cap{position:absolute;left:0;bottom:0;width:100%;background:rgba(255,106,19,.85);color:var(--white);display:flex;align-items:center;padding-left:11px;font-family:"Montserrat",sans-serif}
.card-cap strong{font-size:17px;letter-spacing:3px;font-weight:600}
.card-cap span{font-family:"Raleway",sans-serif;font-size:9px;margin-left:10px}
.card-cap span::before{content:"|";margin-right:8px}

/* newsletter + footer */
.news-bar{left:0;top:2718px;width:1200px;height:54px;background:var(--footer)}
.news-icon{left:157px;top:2731px;width:30px;height:30px;border-radius:50%;background:var(--white);display:flex;align-items:center;justify-content:center}
.news-label{left:201px;top:2736px;color:var(--white);font-family:"Montserrat",sans-serif;font-size:15px;font-weight:600;letter-spacing:2.5px}
.news-input{left:600px;top:2724px;width:347px;height:41px;background:var(--white);font-size:9px;color:#999;padding:15px 14px}
.btn-send{left:955px;top:2724px;width:101px;height:41px;font-size:14px;font-weight:600;gap:12px}
.footer{left:0;top:2772px;width:1200px;height:296px;background:var(--footer)}
.footer-brand{left:160px;top:2855px;width:250px;text-align:center;color:var(--white);font-family:"Montserrat",sans-serif;font-size:26px;font-weight:700;letter-spacing:2px;line-height:36px}
.footer-brand .brand-mark{display:block;width:60px;height:60px;margin:0 auto 22px;margin-right:auto}
.social{top:3019px;width:30px;height:30px;border-radius:50%;background:#1d6fd1}
.f-head{top:2803px;color:var(--white);font-family:"Montserrat",sans-serif;font-size:18px;font-weight:600;letter-spacing:3px}
.f-list{list-style:none;top:2858px;color:var(--white);font-size:9.5px}
.f-list li{height:26.5px;display:flex;align-items:flex-start;gap:8px}
.f-list li::before{content:"\2713";font-size:9px}
.f-contact{color:var(--white);font-size:10px;display:flex;align-items:center;gap:8px}
.f-rule{left:455px;top:3000px;width:602px;height:1px;background:var(--footer-rule)}
.copy{right:144px;top:3028px;color:var(--white);font-size:9.5px}
</style>
</head>
<body>

<!-- hero -->
<svg class="abs hero-bg" viewBox="0 0 1200 660" role="img" aria-label="Photograph looking up at glass skyscrapers">
  <defs>
    <linearGradient id="heroShade" x1="0" y1="0" x2="1" y2="1">
      <stop offset="0" stop-color="#2d3946"/>
      <stop offset=".5" stop-color="#1b242e"/>
      <stop offset="1" stop-color="#3c4957"/>
    </linearGradient>
  </defs>
  <rect width="1200" height="660" fill="url(#heroShade)"/>
  <polygon points="0,565 1200,650 1200,660 0,660" fill="var(--orange)"/>
  <polygon points="0,570 1200,660 0,660" fill="#ffffff"/>
</svg>

<div class="abs brand"><span class="brand-mark"></span><span class="brand-name">SUMMIT</span></div>
<nav class="abs nav">
  <a href="#" style="left:0">Home</a>
  <a href="#" style="left:77px">About Us</a>
  <a href="#" style="left:172px">Services</a>
  <a href="#" style="left:260px">Our Projects</a>
  <span style="position:absolute;left:340px;color:#fff">|</span>
</nav>
<svg class="abs search" width="16" height="16" viewBox="0 0 16 16" aria-label="Search"><circle cx="7" cy="7" r="5.5" fill="none" stroke="#fff" stroke-width="1.3"/><line x1="11" y1="11" x2="15" y2="15" stroke="#fff" stroke-width="1.3"/></svg>
<a class="abs btn btn-contact" href="#">CONTACT US</a>

<div class="abs hero-title big">SUMMIT</div>
<div class="abs hero-title light">BUILDERS</div>
<div class="abs hero-tag">THE BEST CHOOSE US Because We Deliver</div>
<a class="abs btn btn-hero" href="#">Learn More</a>
<svg class="abs scroll-cue" width="24" height="42" viewBox="0 0 24 42" aria-hidden="true">
  <rect x="6" y="1" width="12" height="18" rx="6" fill="none" stroke="#fff" stroke-width="1.3"/>
  <line x1="12" y1="5" x2="12" y2="9" stroke="#fff" stroke-width="1.3"/>
  <polyline points="6,25 12,30 18,25" fill="none" stroke="#fff" stroke-width="1.3"/>
  <polyline points="6,32 12,37 18,32" fill="none" stroke="#fff" stroke-width="1.3"/>
</svg>

<!-- about -->
<div class="abs about-kicker">ABOUT</div>
<h1 class="abs about-title">SUMMIT BUILDERS</h1>
<div class="abs about-copy">
  <p>Construction Company that specializes in Water and Fire Damage, Residential ReModels, Landscaping and Building ADU (Accessory Dwelling Unit)<br>Growing and changing families often need additional space, and a remodeling project can often provide that. Adding a new area, or repurposing an existing one can satisfy this requirement.</p>
  <p>Other times, homeowners want to update the look in their kitchen or bathroom with more than just a change of cabinetry or vanity doors and drawers. Whatever your needs are, Summit Builders has skilled workers who are bonded and</p>
</div>
<a class="abs btn btn-about" href="#">Learn More</a>
<svg class="abs about-photo" width="368" height="358" viewBox="0 0 368 358" role="img" aria-label="Builder carrying a hammer beside timber framing under a blue sky">
  <defs>
    <linearGradient id="aboutPhoto" x1="0" y1="0" x2="1" y2="1">
      <stop offset="0" stop-color="#4d86c9"/>
      <stop offset=".55" stop-color="#d9b47a"/>
      <stop offset="1" stop-color="#3a3530"/>
    </linearGradient>
  </defs>
  <polygon points="160,0 320,120 320,358 0,358 0,120" fill="url(#aboutPhoto)"/>
</svg>

<!-- stats -->
<div class="abs stat stat-a" role="img" aria-label="Modern house at dusk"><div class="stat-num">53</div><div class="stat-label">TOTAL<br>PROJECTS</div></div>
<div class="abs stat stat-b" role="img" aria-label="Workers in hard hats on site"><div class="stat-num">15</div><div class="stat-label">WORKING IN<br>STATES</div></div>
<div class="abs stat stat-c" role="img" aria-label="Crew reviewing plans at a framed building"><div class="stat-num">2,600</div><div class="stat-label">HOURS FOR<br>WORK</div></div>

<!-- services -->
<svg class="abs services-bg" width="1200" height="675" viewBox="0 0 1200 675" role="img" aria-label="Carpenters working in a workshop, tinted orange">
  <defs>
    <linearGradient id="svcTint" x1="0" y1="0" x2="1" y2="1">
      <stop offset="0" stop-color="#ff7424"/>
      <stop offset=".5" stop-color="#f56a17"/>
      <stop offset="1" stop-color="#ff7a2c"/>
    </linearGradient>
  </defs>
  <polygon points="0,0 1200,48 1200,604 0,672" fill="url(#svcTint)"/>
</svg>
<div class="abs svc-kicker">OUR SERVICES</div>
<h2 class="abs svc-title">WHAT STAGE IS YOUR BUILDING?</h2>
<p class="abs svc-intro">Ut at neque blandit, hendrerit massa et, sodales ipsum. Sed eget urna tempor, porttitor leo et, interdum ex. Aenean sodales eros id rutrum tempus. Aenean in nisl sem. Sed interdum, felis vitae ultrices cursus, neque libero vestibulum neque,</p>

<div class="abs svc-rule" style="left:442px"></div>
<div class="abs svc-rule" style="left:755px"></div>

<div class="abs svc-col" style="left:131px">
  <svg width="48" height="50" viewBox="0 0 48 50" aria-hidden="true" fill="none" stroke="#fff" stroke-width="1.8"><polyline points="4,24 24,8 44,24"/><rect x="9" y="22" width="30" height="24"/><rect x="20" y="32" width="8" height="14"/><path d="M16 6c2-4 6-2 4 2M28 4c2-3 6 0 3 3"/></svg>
  <h3>Water and Fire Damage</h3>
  <p>Ut at neque blandit, hendrerit massa et, sodales ipsum. Sed eget urna tempor, porttitor leo et, interdum ex. Aenean</p>
  <a href="#">Read More</a>
</div>
<div class="abs svc-col" style="left:449px">
  <svg width="56" height="52" viewBox="0 0 56 52" aria-hidden="true" fill="none" stroke="#fff" stroke-width="2.2"><polyline points="3,26 28,4 53,26"/><polyline points="10,20 10,49 46,49 46,20"/><path d="M22 49V34a6 6 0 0 1 12 0v15"/></svg>
  <h3>Residential ReModels</h3>
  <p>Aenean sodales eros id rutrum tempus. Aenean in nisl sem. Sed interdum, felis vitae ultrices cursus, neque libero vestibulum</p>
  <a href="#">Read More</a>
</div>
<div class="abs svc-col" style="left:764px">
  <svg width="52" height="56" viewBox="0 0 52 56" aria-hidden="true" fill="none" stroke="#fff" stroke-width="1.8"><rect x="3" y="3" width="26" height="51"/><rect x="29" y="20" width="20" height="34"/><path d="M9 10h4M19 10h4M9 18h4M19 18h4M9 26h4M19 26h4M9 34h4M19 34h4M35 28h4M35 36h4M35 44h4"/></svg>
  <h3>Landscaping and Building</h3>
  <p>Ut at neque blandit, hendrerit massa et, sodales ipsum. Sed eget urna tempor, porttitor leo et, interdum ex.</p>
  <a href="#">Read More</a>
</div>

<!-- projects -->
<h2 class="abs proj-title">OUR PROJECTS</h2>
<p class="abs proj-intro">Ut at neque blandit, hendrerit massa et, sodales ipsum. Sed eget urna tempor, porttitor leo et, interdum ex. Aenean sodales eros id rutrum tempus. Aenean in nisl sem. Sed interdum, felis vitae ultrices cursus</p>

<div class="abs card" style="left:0;top:2312px;width:274px;height:313px">
  <div class="card-photo" role="img" aria-label="Brick two-storey family house" style="background:linear-gradient(180deg,#4f8fd6 0%,#9dbfe0 45%,#8a6a58 75%,#4d6b3a 100%)"></div>
  <div class="card-cap" style="height:50px"><strong>Expansion</strong><span>Los Angeles, CA</span></div>
</div>
<div class="abs card" style="left:298px;top:2283px;width:603px;height:371px">
  <div class="card-photo" role="img" aria-label="Curved stone high school building with glass wing" style="background:linear-gradient(100deg,#e6dccd 0%,#d8ccb8 45%,#4f89c4 60%,#6b5a4c 100%)"></div>
  <div class="card-cap" style="height:60px;padding-left:42px"><strong style="font-size:20px">Title Here</strong><span>State Here</span></div>
</div>
<div class="abs card" style="left:925px;top:2312px;width:275px;height:313px">
  <div class="card-photo" role="img" aria-label="Grey suburban house at dusk with lit garage" style="background:linear-gradient(180deg,#7b8fb6 0%,#c9b3c2 40%,#6e7380 70%,#4e5560 100%)"></div>
  <div class="card-cap" style="height:50px;padding-left:23px"><strong>Title Here</strong><span>Las Vegas, NV</span></div>
</div>

<!-- newsletter -->
<div class="abs news-bar"></div>
<div class="abs news-icon"><svg width="14" height="14" viewBox="0 0 14 14" aria-hidden="true"><polygon points="1,6 13,1 8,13 7,8" fill="none" stroke="var(--orange)" stroke-width="1.2"/></svg></div>
<div class="abs news-label">Subscribe To Newsletter</div>
<div class="abs news-input">Send a Message...</div>
<a class="abs btn btn-send" href="#">Send <svg width="18" height="8" viewBox="0 0 18 8" aria-hidden="true"><line x1="0" y1="4" x2="16" y2="4" stroke="#fff"/><polyline points="13,1 17,4 13,7" fill="none" stroke="#fff"/></svg></a>

<!-- footer -->
<div class="abs footer"></div>
<div class="abs footer-brand"><span class="brand-mark"></span>SUMMIT<br>BUILDERS</div>
<div class="abs social" style="left:231px" role="img" aria-label="Social profile"></div>
<div class="abs social" style="left:271px" role="img" aria-label="Social profile"></div>
<div class="abs social" style="left:311px" role="img" aria-label="Social profile"></div>

<div class="abs f-head" style="left:464px">Services</div>
<ul class="abs f-list" style="left:465px">
  <li>Water and Fire Damage</li>
  <li>Residential ReModels</li>
  <li>Landscaping and Building ADU</li>
</ul>
<div class="abs f-head" style="left:693px">Site Map</div>
<ul class="abs f-list" style="left:690px">
  <li>Home</li>
  <li>About Us</li>
  <li>Services</li>
  <li>Our Projects</li>
  <li>Contact Us</li>
</ul>
<div class="abs f-head" style="left:881px">Get In Touch</div>
<div class="abs f-contact" style="left:892px;top:2858px"><svg width="14" height="14" viewBox="0 0 14 14" aria-hidden="true"><path d="M3 1l2 3-1.5 1.5a8 8 0 0 0 5 5L10 9l3 2-1 2c-6 0-11-5-11-11z" fill="none" stroke="#fff" stroke-width="1"/></svg>+1 555 014 7720</div>
<div class="abs f-contact" style="left:892px;top:2893px"><svg width="14" height="10" viewBox="0 0 14 10" aria-hidden="true"><rect x=".5" y=".5" width="13" height="9" fill="none" stroke="#fff"/><polyline points=".5,.5 7,6 13.5,.5" fill="none" stroke="#fff"/></svg>info@summitbuildersca.example</div>
<div class="abs f-rule"></div>
<div class="abs copy">© 2020 SUMMIT BUILDERS - ALL RIGHTS RESERVED.</div>

</body>
</html>
```